Hexagon Honey Bottle Design, simple and elegant.

Bottle description:
BODY HEIGHT With cap 8.75cm
Without cap 8.6cm
DIAMETER Inner 4.4cm
Outer 5.2cm
Label height only has to be = 6cm height x (3.4X6) length of one hexagonal box is 3.4cm
See through bottle with black cap.
Concept of design:
Elegant, Simple, no pictures of bees, pictures of honeycomb, wooden honey stick, or drooling honey from either is ok. Simple colors. (Designer's discretion)
Wordings:
Hex1
Product of Yemen
Header:
MAROL /TUVI/ (Brand name)
Explanatory below header
Yemen Sidr Honey from The Valley Qarbeen (100% Pure)
(name of honey)
250g
Optional
Hex2
Pure
=
No Additives (not even natural additives)
Hex3
Raw
=
Unheated, Unpasteurized, Unprocessed honey
Hex4
Natural
=
No added color, artificial flavor, or synthetic substance
Hex5
RENOWNED
=
Very well known by honey lovers
(Natural Pure Raw and Renowned) wordings to be on a suitable place on the bottle (maybe on the cap) -
Hex6
Imported By
The Copperfield Trading Pte Ltd
No. 317, Larkspur Grove Road, #09-12
Larkspur Grove Plaza
Singapore 174593
Wordings can be rearranged - its up to the designer's discretion where and how to place them and in which order.-
Designer must be willing to do numerous changes as the design develops

```html
<!DOCTYPE html>
<html lang="en">
<head>
<meta charset="utf-8">
<title>MAROL Honey Label</title>
<link rel="stylesheet" href="https://fonts.googleapis.com/css2?family=Oswald:wght@300;500;600&family=Pathway+Gothic+One&family=Dancing+Script&family=Comfortaa:wght@400&family=Poppins:wght@400&display=swap">
<style>
  :root {
    --bg: #e9e7e2;
    --ink: #231f20;
    --cap: #1c1a1a;
    --gold: #c9a24a;
    --honey-deep: #f4b419;
    --honey-light: #f8c34e;
    --white: #ffffff;
  }
  * { box-sizing: border-box; margin: 0; padding: 0; }
  html, body { width: 1200px; height: 894px; overflow: hidden; background: var(--bg); }
  .canvas { position: relative; width: 1200px; height: 894px; }

  .cap-band {
    position: absolute; left: 30px; top: 170px; width: 1140px; height: 72px;
    background: var(--cap); border-radius: 10px;
    display: flex; align-items: center; justify-content: center;
    font-family: "Comfortaa", sans-serif; font-size: 26px; color: var(--gold); letter-spacing: 1px;
  }

  .label {
    position: absolute; left: 30px; top: 280px; width: 1140px; height: 360px;
    display: flex; border-top: 8px solid var(--ink); border-bottom: 8px solid var(--ink);
  }
  .panel { width: 190px; height: 100%; position: relative; text-align: center; color: var(--ink); }
  .panel--deep { background: var(--honey-deep); }
  .panel--light { background: var(--honey-light); }

  .keyword {
    margin-top: 116px;
    font-family: "Oswald", sans-serif; font-weight: 500; font-size: 20px;
    letter-spacing: 4px; text-transform: uppercase; line-height: 1;
  }
  .equals { font-family: "Oswald", sans-serif; font-weight: 600; font-size: 20px; margin-top: 22px; line-height: 1; }
  .script { font-family: "Dancing Script", cursive; font-size: 15px; line-height: 1.4; margin-top: 22px; padding: 0 12px; }

  .front { padding-top: 22px; }
  .front__origin { font-family: "Poppins", sans-serif; font-size: 10px; color: var(--white); }
  .front__rule { width: 110px; height: 1px; background: var(--white); margin: 3px auto 0; }
  .front__brand { font-family: "Oswald", sans-serif; font-weight: 300; font-size: 30px; letter-spacing: 6px; color: var(--white); margin-top: 4px; line-height: 1.1; }
  .front__dipper { position: absolute; left: 14px; top: 98px; width: 22px; height: 160px; background: var(--white); opacity: .9; }
  .front__pure { position: absolute; right: 12px; top: 98px; font-family: "Oswald", sans-serif; font-weight: 300; font-size: 19px; line-height: 1.2; }
  .front__bar { position: absolute; left: 36px; right: 0; top: 130px; height: 5px; background: var(--ink); }
  .front__name { position: absolute; right: 12px; top: 142px; font-family: "Oswald", sans-serif; font-weight: 600; font-size: 34px; line-height: 1.08; text-align: right; }
  .front__weight { position: absolute; right: 14px; top: 228px; background: var(--ink); color: var(--honey-light); border-radius: 14px; padding: 0 12px; font-family: "Oswald", sans-serif; font-weight: 300; font-size: 17px; line-height: 1.5; }
  .front__variety { position: absolute; left: 0; right: 0; bottom: 30px; font-family: "Pathway Gothic One", sans-serif; font-size: 22px; line-height: 1.1; }
  .front__variety span { display: block; font-size: 16px; }

  .imported { padding-top: 140px; font-family: "Pathway Gothic One", sans-serif; font-size: 15px; line-height: 2; }
  .imported__title { font-family: "Oswald", sans-serif; font-weight: 500; font-size: 14px; }
</style>
</head>
<body>
<div class="canvas">
  <div class="cap-band">Natural Pure Raw and Renowned</div>

  <div class="label">
    <section class="panel panel--light">
      <h2 class="keyword">Natural</h2>
      <div class="equals">=</div>
      <p class="script">No added color,<br>artificial flavor,<br>or synthetic substance</p>
    </section>

    <section class="panel panel--deep front">
      <p class="front__origin">Product of Yemen</p>
      <div class="front__rule"></div>
      <p class="front__brand">MAROL</p>
      <div class="front__dipper" role="img" aria-label="Illustration of a honey dipper with dripping honey"></div>
      <p class="front__pure">100% PURE</p>
      <div class="front__bar"></div>
      <h1 class="front__name">NATURAL<br>HONEY</h1>
      <p class="front__weight"><i>250g</i></p>
      <p class="front__variety">Yemen Sidr Honey<span>from The Valley QARBEEN</span></p>
    </section>

    <section class="panel panel--light">
      <h2 class="keyword">Pure</h2>
      <div class="equals">=</div>
      <p class="script">No Additives<br>(not even natural additives)</p>
    </section>

    <section class="panel panel--deep">
      <h2 class="keyword">Raw</h2>
      <div class="equals">=</div>
      <p class="script">Unheated,<br>Unpasteurized,<br>Unprocessed honey</p>
    </section>

    <section class="panel panel--light imported">
      <p class="imported__title">IMPORTED BY</p>
      <p>The Copperfield Trading Pte Ltd</p>
      <p>No. 317, Larkspur Grove Road, #09-12</p>
      <p>Larkspur Grove Plaza</p>
      <p>Singapore 174593</p>
    </section>

    <section class="panel panel--deep">
      <h2 class="keyword">Renowned</h2>
      <div class="equals">=</div>
      <p class="script">Very well known<br>by<br>honey lovers</p>
    </section>
  </div>
</div>
</body>
</html>
```